Business Card for Industrial Distributor

We need a business card design for an industrial distributor. We sell machine parts for the manufacturing and oil industry. We would like the cards to look clean and modern but with a touch of industry.

Our colors are blue/white.

Please feel free to visit our website www.krovelmint.com

Target Market(s)

mexican manufacturers in the automobile/aerospace industry

Industry/Entity Type

Industrial

Colors
ffffff
0555a3

```html
<!DOCTYPE html>
<html lang="en">
<head>
<meta charset="utf-8">
<title>Krovelmint Business Card</title>
<link href="https://fonts.googleapis.com/css2?family=Exo+2:ital,wght@1,800&family=Roboto:wght@300;400&display=swap" rel="stylesheet">
<style>
  :root {
    --brand-blue: #0555a3;
    --brand-blue-deep: #0a3f8f;
    --brand-blue-light: #1a6fd0;
    --white: #ffffff;
    --paper-grey: #e9eaec;
    --text-dark: #3a3a3a;
    --backdrop: #d9d4cb;
  }
  * { margin: 0; padding: 0; box-sizing: border-box; }
  html, body { width: 1200px; height: 1023px; overflow: hidden; }
  body {
    background: var(--backdrop);
    position: relative;
    font-family: "Roboto", sans-serif;
  }
  .card {
    position: absolute;
    width: 540px;
    height: 308px;
    border-radius: 14px;
    overflow: hidden;
    box-shadow: 0 10px 24px rgba(0,0,0,0.25);
  }

  /* Front */
  .card-front {
    left: 70px; top: 150px;
    background: linear-gradient(135deg, var(--white) 30%, var(--paper-grey) 100%);
    border-bottom: 8px solid var(--brand-blue);
  }
  .front-rule {
    position: absolute; left: 0; right: 0; top: 148px;
    height: 3px; background: var(--brand-blue-deep);
  }
  .front-brand {
    position: absolute; left: 40px; top: 112px;
    display: flex; align-items: center; gap: 12px;
    background: linear-gradient(135deg, var(--white) 0%, #f4f4f5 100%);
    padding: 0 14px;
  }
  .brand-dot {
    width: 46px; height: 46px; border-radius: 50%;
    background: var(--brand-blue-light);
  }
  .brand-name {
    font-family: "Exo 2", sans-serif;
    font-weight: 800; font-style: italic;
    font-size: 56px; line-height: 1;
    color: var(--brand-blue-deep);
    letter-spacing: -1px;
  }
  .holder {
    position: absolute; right: 34px; top: 40px; text-align: right;
  }
  .holder-name { font-size: 26px; font-weight: 400; color: var(--text-dark); letter-spacing: 1px; }
  .holder-title { font-size: 14px; font-weight: 300; color: var(--brand-blue-light); letter-spacing: 1px; }
  .contacts {
    position: absolute; right: 34px; top: 172px;
    list-style: none; text-align: right;
    font-size: 12px; color: var(--text-dark); letter-spacing: 1px; line-height: 22px;
  }
  .contacts li { display: flex; justify-content: flex-end; align-items: center; gap: 8px; }
  .contacts svg { width: 12px; height: 12px; }
  .address {
    position: absolute; left: 40px; bottom: 22px;
    display: flex; align-items: flex-end; gap: 8px;
    font-size: 12px; color: var(--text-dark); letter-spacing: 1px; line-height: 17px;
  }
  .address svg { width: 10px; height: 14px; margin-bottom: 2px; }

  /* Back */
  .card-back {
    left: 590px; top: 560px;
    background: linear-gradient(160deg, var(--brand-blue-deep) 0%, var(--brand-blue) 60%, #0b4aa8 100%);
    display: flex; flex-direction: column; align-items: center; justify-content: center; gap: 18px;
  }
  .back-brand { display: flex; align-items: center; gap: 16px; }
  .back-brand .brand-dot { width: 62px; height: 62px; background: var(--white); }
  .back-brand .brand-name { color: var(--white); font-size: 70px; }
  .back-url {
    font-size: 13px; letter-spacing: 4px; color: var(--white); font-weight: 300;
  }
</style>
</head>
<body>
  <section class="card card-front" aria-label="Business card front">
    <div class="front-rule"></div>
    <div class="front-brand">
      <span class="brand-dot"></span>
      <span class="brand-name">Krovelmint</span>
    </div>
    <div class="holder">
      <p class="holder-name">Your Name</p>
      <p class="holder-title">Title</p>
    </div>
    <ul class="contacts">
      <li>(512) 730-4418
        <svg viewBox="0 0 12 12"><circle cx="6" cy="6" r="5.5" fill="none" stroke="#0555a3"/><path d="M4 3.5l1 1.5-.6.8a4 4 0 0 0 1.8 1.8l.8-.6 1.5 1-.7 1A5 5 0 0 1 3 4.2z" fill="#0555a3"/></svg>
      </li>
      <li>(512) 730-4426
        <svg viewBox="0 0 12 12"><rect x="1.5" y="3" width="9" height="8" fill="#0555a3"/><rect x="3" y="1" width="6" height="3" fill="none" stroke="#0555a3"/></svg>
      </li>
      <li>sales@krovelmint.com
        <svg viewBox="0 0 12 12"><rect x="1" y="2.5" width="10" height="7" fill="none" stroke="#0555a3"/><path d="M1 2.5l5 4 5-4" fill="none" stroke="#0555a3"/></svg>
      </li>
      <li>www.krovelmint.com
        <svg viewBox="0 0 12 12"><circle cx="6" cy="6" r="5" fill="#0555a3"/><path d="M1 6h10M6 1v10M2.5 3.5h7M2.5 8.5h7" stroke="#fff" stroke-width=".7"/></svg>
      </li>
    </ul>
    <div class="address">
      <svg viewBox="0 0 10 14"><path d="M5 0a5 5 0 0 1 5 5c0 3.5-5 9-5 9S0 8.5 0 5a5 5 0 0 1 5-5z" fill="#0555a3"/><circle cx="5" cy="5" r="1.8" fill="#fff"/></svg>
      <p>4120 Harlow Ridge Rd<br>Calderon, TX 78990</p>
    </div>
  </section>

  <section class="card card-back" aria-label="Business card back">
    <div class="back-brand">
      <span class="brand-dot"></span>
      <span class="brand-name">Krovelmint</span>
    </div>
    <p class="back-url">www.krovelmint.com</p>
  </section>
</body>
</html>
```